Business Cards and Stationary for Dental Office
Modern dental office
I need double sided standard sized Business Card [3.5" x 2"]
You can use either the same font, or change it up--as long as it looks good
Bright & Fun-filled
Folasade Ikeribe DDS
Dr.
5128 Marlow Ave
Suite 210
Baltimore, MD 21229
TBD
Info@mycedarlinedental.com
www.mycedarlinedental.com
The phone number is tbd
Please note this as I will ask for it to be added at a later date. Thanks
This is my logo in AI

```html
<!DOCTYPE html>
<html lang="en">
<head>
<meta charset="utf-8">
<title>Cedarline Dental Care – Business Card</title>
<link href="https://fonts.googleapis.com/css2?family=Cinzel:wght@400&family=Raleway:wght@400;500&display=swap" rel="stylesheet">
<style>
  :root {
    --backdrop: #d8d9d9;
    --card: #ffffff;
    --mint: #a9d8b6;
    --mint-deep: #7fbf92;
    --stone: #9a9c9e;
    --ink: #6f7275;
    --ink-soft: #8d9093;
  }
  * { box-sizing: border-box; margin: 0; padding: 0; }
  html, body { width: 1200px; height: 984px; overflow: hidden; }
  body {
    background: var(--backdrop);
    display: flex;
    flex-direction: column;
    align-items: center;
    justify-content: center;
    gap: 40px;
    font-family: "Raleway", sans-serif;
  }
  .card {
    position: relative;
    width: 760px;
    height: 434px;
    background: var(--card);
    border-radius: 26px;
    overflow: hidden;
    box-shadow: 0 6px 18px rgba(0,0,0,.12);
  }
  .card-corners { position: absolute; inset: 0; width: 100%; height: 100%; }
  .mint { fill: var(--mint); }
  .stone { fill: var(--stone); }

  .brand {
    position: absolute;
    display: flex;
    flex-direction: column;
    align-items: center;
    text-align: center;
  }
  .brand-dot {
    width: 46px; height: 46px;
    border-radius: 50%;
    background: var(--mint-deep);
    margin-bottom: 16px;
  }
  .brand-name {
    font-family: "Cinzel", serif;
    font-size: 30px;
    letter-spacing: 1px;
    color: var(--ink);
    white-space: nowrap;
  }
  .brand-tagline {
    font-family: "Raleway", sans-serif;
    font-size: 12px;
    letter-spacing: 2px;
    text-transform: uppercase;
    color: var(--mint-deep);
    margin-top: 6px;
  }
  .card-front .brand { left: 0; right: 0; top: 130px; }

  .card-back .brand { left: 40px; width: 320px; top: 140px; }
  .card-back .brand-name { font-size: 24px; }
  .card-back .brand-tagline { font-size: 10px; }
  .divider {
    position: absolute;
    left: 385px; top: 110px;
    width: 1px; height: 214px;
    background: var(--stone);
  }
  .contact { position: absolute; left: 410px; top: 112px; }
  .contact-name {
    font-family: "Cinzel", serif;
    font-size: 19px;
    color: var(--mint-deep);
  }
  .contact-role {
    font-size: 12px;
    letter-spacing: 1px;
    color: var(--ink-soft);
    margin-top: 2px;
    margin-bottom: 22px;
  }
  .contact-list { list-style: none; }
  .contact-list li {
    display: flex;
    align-items: center;
    gap: 10px;
    font-size: 13px;
    color: var(--ink);
    line-height: 1.25;
    margin-bottom: 8px;
  }
  .contact-list svg { width: 14px; height: 14px; flex: none; fill: var(--mint-deep); }
</style>
</head>
<body>

<section class="card card-front" aria-label="Card front">
  <svg class="card-corners" viewBox="0 0 760 434" aria-hidden="true">
    <path class="mint" d="M0,190 L0,50 Q0,0 50,0 L260,0 Q50,12 0,190 Z"/>
    <path class="stone" d="M760,120 L760,40 Q760,0 720,0 L620,0 Q740,8 760,120 Z"/>
    <path class="stone" d="M0,314 L0,394 Q0,434 40,434 L140,434 Q20,426 0,314 Z"/>
    <path class="mint" d="M760,244 L760,384 Q760,434 710,434 L500,434 Q710,422 760,244 Z"/>
  </svg>
  <div class="brand">
    <span class="brand-dot"></span>
    <h1 class="brand-name">Cedarline Dental Care</h1>
    <p class="brand-tagline">Cosmetic &amp; General Dentistry</p>
  </div>
</section>

<section class="card card-back" aria-label="Card back">
  <svg class="card-corners" viewBox="0 0 760 434" aria-hidden="true">
    <path class="stone" d="M0,200 L0,50 Q0,0 50,0 L270,0 Q40,14 0,200 Z"/>
    <path class="mint" d="M0,140 L0,40 Q0,12 30,8 L180,8 Q30,22 0,140 Z"/>
    <path class="stone" d="M760,234 L760,384 Q760,434 710,434 L490,434 Q720,420 760,234 Z"/>
    <path class="mint" d="M760,294 L760,394 Q760,422 730,426 L580,426 Q730,412 760,294 Z"/>
  </svg>
  <div class="brand">
    <span class="brand-dot"></span>
    <h2 class="brand-name">Cedarline Dental Care</h2>
    <p class="brand-tagline">Cosmetic &amp; General Dentistry</p>
  </div>
  <span class="divider"></span>
  <div class="contact">
    <p class="contact-name">Folasade Ikeribe DDS</p>
    <p class="contact-role">Dentist</p>
    <ul class="contact-list">
      <li>
        <svg viewBox="0 0 14 14"><path d="M7,0 C3.7,0 1.5,2.4 1.5,5.3 C1.5,9 7,14 7,14 C7,14 12.5,9 12.5,5.3 C12.5,2.4 10.3,0 7,0 Z M7,7.4 A2.1,2.1 0 1 1 7,3.2 A2.1,2.1 0 1 1 7,7.4 Z"/></svg>
        5128 Marlow Ave, Suite 210, Baltimore, MD 21229
      </li>
      <li>
        <svg viewBox="0 0 14 14"><path d="M3,0.5 L5.2,3.6 L3.8,5 Q5,8 9,10.2 L10.4,8.8 L13.5,11 L12,13.5 Q5,13.5 0.5,2 Z"/></svg>
        Office: (410) 555-0142
      </li>
      <li>
        <svg viewBox="0 0 14 14"><path d="M3,0 H10 V4 H3 Z M1,5 H13 V11 H11 V14 H3 V11 H1 Z M4.5,9 V12.5 H9.5 V9 Z"/></svg>
        Fax: (410) 555-0178
      </li>
      <li>
        <svg viewBox="0 0 14 14"><path d="M0,2.5 H14 V11.5 H0 Z M1.2,3.6 L7,8 L12.8,3.6 Z"/></svg>
        Info@mycedarlinedental.com
      </li>
      <li>
        <svg viewBox="0 0 14 14"><path d="M7,0 A7,7 0 1 0 7,14 A7,7 0 1 0 7,0 Z M7,1.4 Q9.4,3.5 9.4,7 Q9.4,10.5 7,12.6 Q4.6,10.5 4.6,7 Q4.6,3.5 7,1.4 Z M1.6,6.3 H12.4 V7.7 H1.6 Z"/></svg>
        www.mycedarlinedental.com
      </li>
    </ul>
  </div>
</section>

</body>
</html>
```